WordPress Website for Pain Relief Clinic

I need a WordPress website designed for my laser pain relief clinic. It needs to be a professional, responsive design with 7 pages: Home, Why Choose Us, Treatable Conditions, Testimonials, FAQ, Franchising, Contact Us. Here is logo: https://s3.cloudvexa-store.net/media.b-r-t-n.net/sitebuilder/361/KelvaroLogoHighQuality.png

Target Market(s)

people with pain,elderly adults,injuries,soreness

Industry/Entity Type

Clinic

Number of Pages Required

5+ page

Colors
0792cd
85abd2

```html
<!DOCTYPE html>
<html lang="en">
<head>
<meta charset="utf-8">
<title>Kelvaro Laser Pain Relief</title>
<link href="https://fonts.googleapis.com/css2?family=Archivo+Black&family=Arimo:wght@400;700&family=Noto+Serif:wght@400;700&family=Open+Sans:wght@400;600;700&family=Oswald:wght@600&display=swap" rel="stylesheet">
<style>
:root{
  --blue:#0792cd;
  --blue-tile:#1a78c8;
  --blue-nav:#3d7fcf;
  --blue-nav-light:#5a9ae0;
  --navy:#1b3c8c;
  --pink:#e0115f;
  --orange:#f7941d;
  --tile:#e2eaf3;
  --text:#444;
  --muted:#8a8a8a;
  --footer:#ebebeb;
}
*{box-sizing:border-box;margin:0;padding:0}
html,body{width:889px;height:1200px;overflow:hidden;background:#fff}
body{position:relative;font-family:"Open Sans",Arial,sans-serif;color:var(--text)}
.abs{position:absolute}

/* header */
.brand{left:78px;top:18px;display:flex;align-items:center;gap:10px}
.brand-mark{width:44px;height:44px;border-radius:50%;background:var(--tile)}
.brand-name{font-family:"Noto Serif",serif;font-weight:700;font-size:28px;color:var(--navy);line-height:1}
.brand-tag{left:132px;top:50px;font-family:"Noto Serif",serif;font-size:12.5px;letter-spacing:1.5px;color:#555}
.call{right:74px;top:20px;width:206px;text-align:center}
.call-label{font-size:11px;color:#999;display:flex;align-items:center;gap:6px}
.call-label::before,.call-label::after{content:"";flex:1;height:1px;background:#ddd}
.call-num{font-size:21px;letter-spacing:1px;color:#666;margin-top:2px}

/* nav */
.nav{left:0;top:82px;width:889px;height:40px;background:linear-gradient(var(--blue-nav-light),var(--blue-nav));display:flex;padding-left:74px}
.nav a{display:flex;align-items:center;justify-content:center;height:40px;color:#fff;text-decoration:none;font-size:10.5px;border-left:1px solid rgba(255,255,255,.25);padding:0 14px}
.nav a:last-child{border-right:1px solid rgba(255,255,255,.25)}
.nav a.active{background:rgba(255,255,255,.18);width:84px}

/* hero */
.hero{left:0;top:122px;width:889px;height:320px;background:linear-gradient(90deg,#0b1f55 0%,#13318c 35%,#2a62c8 55%,#7f93b8 78%,#c4aaa6 100%)}
.hero-title{left:74px;top:190px;font-family:"Archivo Black",sans-serif;color:#fff;font-size:31px;line-height:39px}
.hero-copy{left:74px;top:272px;width:240px;font-family:Arimo,Arial,sans-serif;font-size:10px;line-height:13px;color:#c9d6ee}
.hero-btn{left:74px;top:335px;width:160px;height:33px;border-radius:6px;background:var(--pink);color:#fff;font-family:"Oswald",sans-serif;font-size:12.5px;letter-spacing:.5px;display:flex;align-items:center;justify-content:center}

/* welcome */
.welcome{left:0;top:466px;width:889px;text-align:center;font-family:"Noto Serif",serif;font-weight:700;font-size:25px;color:var(--navy)}
.welcome span{color:var(--pink)}
.intro{left:90px;top:513px;width:709px;text-align:center;font-family:Arimo,Arial,sans-serif;font-size:12.4px;line-height:18px;color:var(--muted)}

/* feature cards */
.card{top:606px;width:231px;height:193px;border:1px solid #ddd;box-shadow:0 8px 6px -6px rgba(0,0,0,.45)}
.card-img{height:159px}
.card-label{height:33px;background:var(--pink);color:#fff;font-family:Arimo,Arial,sans-serif;font-size:13px;display:flex;align-items:center;justify-content:center}

/* news */
.news{left:77px;top:855px;width:737px;height:63px;border:1px solid #e3e3e3;display:flex}
.news-date{width:45px;background:#d6d6d6;color:#fff;text-align:center;padding-top:13px}
.news-date b{display:block;font-size:10px;font-weight:600}
.news-date strong{display:block;font-size:18px;line-height:18px}
.news-body{padding:11px 0 0 25px;width:600px;font-family:Arimo,Arial,sans-serif}
.news-head{font-size:11px;color:#222}
.news-text{font-size:9px;line-height:12px;color:#888;margin-top:4px}
.news-arrow{position:absolute;right:10px;top:20px}

/* tiles */
.tile{top:957px;width:182px;height:62px;background:var(--tile);padding:17px 0 0 31px;position:absolute}
.tile.highlight{background:var(--blue-tile)}
.tile-icon{position:absolute;left:2px;top:14px}
.tile h3{font-family:"Archivo Black",sans-serif;font-weight:400;font-size:15px;color:#25406e;line-height:18px}
.tile p{font-size:8px;color:#9aa3ad}
.tile.highlight h3,.tile.highlight p{color:#fff}
.pill{top:1035px;width:182px;height:26px;color:#fff;font-family:Arimo,Arial,sans-serif;font-size:9.5px;display:flex;align-items:center;padding-left:10px}
.pill.blue{background:var(--blue-tile)}
.pill.orange{background:var(--orange)}
.pill svg{position:absolute;right:10px;top:8px}

/* footer */
.footer{left:0;top:1090px;width:889px;height:110px;background:var(--footer)}
.foot-nav{left:75px;top:1107px;display:flex;font-size:10.5px;color:#444}
.foot-nav span{margin-right:37px}
.foot-rule{left:83px;top:1148px;width:711px;height:1px;background:#d0d0d0}
.copy{left:83px;top:1170px;font-size:9.5px;color:#666;word-spacing:1px}
.copy span{margin-left:20px}
.social{left:705px;top:1165px;display:flex;gap:9px}
.social i{width:23px;height:23px;border-radius:50%;display:block}
</style>
</head>
<body>

<header>
  <div class="abs brand"><span class="brand-mark"></span><span class="brand-name">Kelvaro</span></div>
  <div class="abs brand-tag">Laser Pain Relief</div>
  <div class="abs call">
    <div class="call-label">CALL US ON</div>
    <div class="call-num">248-555-0193</div>
  </div>
</header>

<nav class="abs nav">
  <a class="active">HOME</a><a>WHY CHOOSE US</a><a>TREATABLE CONDITIONS</a><a>TESTIMONIALS</a><a>FAQ</a><a>FRANCHISING</a><a>CONTACT US</a>
</nav>

<section>
  <div class="abs hero" role="img" aria-label="Hero photo: glowing blue x-ray torso beside a person holding a painful lower back"></div>
  <h1 class="abs hero-title">Pain Relief<br>Beyond Belief</h1>
  <p class="abs hero-copy">Sed ut perspiciatis unde omnis iste natus error sit voluptatem accusantium doloremque</p>
  <div class="abs hero-btn">BOOK AN APPOINTMENT</div>
</section>

<h2 class="abs welcome">Welcome to <span>Kelvaro</span> Laser Pain Relief</h2>
<p class="abs intro">Sed ut perspiciatis unde omnis iste natus error sit voluptatem accusantium doloremque laudantium, totam rem aperiam, eaque ipsa quae ab illo inventore veritatis et quasi architecto beatae vitae dicta sunt explicabo. Nemo enim ipsam voluptatem quia voluptas sit aspernatur aut odit aut fugit, sed quia consequuntur magni dolores</p>

<div class="abs card" style="left:75px">
  <div class="card-img" role="img" aria-label="Photo: anatomical back with lower spine pain" style="background:linear-gradient(180deg,#2f78d0,#1753a8)"></div>
  <div class="card-label">CONSEQUUNTUR MAGNI</div>
</div>
<div class="abs card" style="left:329px">
  <div class="card-img" role="img" aria-label="Photo: woman holding her sore shoulder" style="background:linear-gradient(180deg,#d8b09a,#b8907c)"></div>
  <div class="card-label">CONSEQUUNTUR MAGNI</div>
</div>
<div class="abs card" style="left:584px">
  <div class="card-img" role="img" aria-label="Photo: person with shoulder pain" style="background:linear-gradient(180deg,#c9d4e0,#aebdcd)"></div>
  <div class="card-label">CONSEQUUNTUR MAGNI</div>
</div>

<div class="abs news">
  <div class="news-date"><b>JUN</b><strong>22</strong></div>
  <div class="news-body">
    <div class="news-head">Sed quia non numquam eius modi tempora incidunt ut labore et dolore magnam aliquam</div>
    <div class="news-text">quasi architecto beatae vitae dicta sunt explicabo. Nemo enim ipsam voluptatem quia voluptas sit aspernatur aut odit aut fugit,<br>sed quia consequuntur magni dolores eos qui ratione voluptatem sequi nesciunt.</div>
  </div>
  <svg class="news-arrow" width="12" height="20" viewBox="0 0 12 20"><path d="M2 2l8 8-8 8" fill="none" stroke="#bbb" stroke-width="2"/></svg>
</div>

<div class="tile" style="left:75px">
  <svg class="tile-icon" width="20" height="28" viewBox="0 0 20 28"><rect x="1" y="4" width="18" height="22" fill="none" stroke="#c8d2dd" stroke-width="2"/><path d="M1 10h18M7 10v16M13 10v16M1 16h18M1 21h18" stroke="#c8d2dd"/></svg>
  <h3>APPOINTMENT</h3><p>We're Here to Get You Better</p>
</div>
<div class="tile" style="left:261px">
  <svg class="tile-icon" width="20" height="28" viewBox="0 0 20 28"><rect x="1" y="4" width="18" height="20" rx="3" fill="#c8d2dd"/><path d="M10 8v12M4 14h12" stroke="#fff" stroke-width="3"/></svg>
  <h3>PAIN CARE</h3><p>It's Time to Get Healthy</p>
</div>
<div class="tile" style="left:446px">
  <svg class="tile-icon" width="20" height="28" viewBox="0 0 20 28"><circle cx="9" cy="9" r="5" fill="#c8d2dd"/><path d="M1 27c0-8 4-11 8-11s8 3 8 11z" fill="#c8d2dd"/></svg>
  <h3>TEAM</h3><p>Pain Laser Clinic Staff</p>
</div>
<div class="tile highlight" style="left:632px">
  <svg class="tile-icon" width="20" height="28" viewBox="0 0 20 28"><path d="M2 3h11l5 5v18H2z" fill="none" stroke="#fff" stroke-width="1.5"/><path d="M13 3v5h5" fill="none" stroke="#fff" stroke-width="1.5"/></svg>
  <h3>CONSULTATION</h3><p>Suffering? Schedule A Consultation</p>
</div>

<div class="abs pill blue" style="left:75px">More About Laser Therapy<svg width="10" height="10" viewBox="0 0 10 10"><path d="M1 9l7-7" stroke="#e03a3a" stroke-width="3"/></svg></div>
<div class="abs pill orange" style="left:261px">More About<svg width="10" height="10" viewBox="0 0 10 10"><path d="M1 9l7-7" stroke="#e03a3a" stroke-width="3"/></svg></div>
<div class="abs pill blue" style="left:446px">Watch Patient Testimonials<svg width="10" height="10" viewBox="0 0 10 10"><path d="M1 9l7-7" stroke="#fff" stroke-width="3"/></svg></div>
<div class="abs pill orange" style="left:632px">View Upcoming Seminars<svg width="10" height="10" viewBox="0 0 10 10"><path d="M1 9l7-7" stroke="#e03a3a" stroke-width="3"/></svg></div>

<footer>
  <div class="abs footer"></div>
  <div class="abs foot-nav"><span>HOME</span><span>WHY CHOOSE US</span><span>TREATABLE CONDITIONS</span><span>TESTIMONIALS</span><span>FAQ</span><span>FRANCHISING</span><span>CONTACT US</span></div>
  <div class="abs foot-rule"></div>
  <div class="abs copy">Copyright ©<span>All rights reserved</span></div>
  <div class="abs social"><i style="background:#3b5a9a"></i><i style="background:#2fb4ea"></i><i style="background:#1e86c0"></i></div>
</footer>

</body>
</html>
```